Poster design for a vet clinic

Running a campaign called 'Pal Spotter', which is where people get a $30 voucher for themselves and their friend if they refer somebody to our vet clinic.

Text something like:
We love Pal Spotters!
Refer a fur friend to our friendly team and both your fur child and their fur child will receive a $30 voucher to use in clinic! *
* Limited to one pet per fur parent and the referred fur parent must be new to our clinic. Unlimited vouchers for number of referrals!

I want it to be cute but professional. You can see the design styles at vettoly.com.au/northryde and see the logo there too.
I am thinking of having a dog whispering to a cat or something like that as the main image.
I would like both the photoshop file and the pdf please. Would be for an A2 poster.

```html
<!DOCTYPE html>
<html lang="en">
<head>
<meta charset="utf-8">
<title>We love Pal Spotters – Referral Poster</title>
<link rel="stylesheet" href="https://fonts.googleapis.com/css2?family=Cookie&family=Open+Sans:wght@400&family=Oswald:wght@500&family=Yellowtail&display=swap">
<style>
  :root {
    --paper: #ffffff;
    --peach: #fae1ca;
    --cocoa: #6e4f44;
    --cream: #f9dcc0;
    --ink: #2b1a10;
    --ginger: #f1a85a;
    --chestnut: #6b3a1f;
    --shadow: #f4c196;
  }
  * { margin: 0; padding: 0; box-sizing: border-box; }
  html, body { width: 1200px; height: 1200px; overflow: hidden; background: var(--paper); }
  .poster { position: relative; width: 1200px; height: 1200px; overflow: hidden; background: var(--paper); }
  .poster__band {
    position: absolute; left: 0; top: 172px; width: 1200px; height: 850px;
    background: var(--peach);
  }
  .brand-box {
    position: absolute; left: 926px; top: 198px; width: 242px; height: 140px;
    background: var(--cocoa);
    display: flex; align-items: center; justify-content: center; gap: 12px;
  }
  .brand-box__dot { width: 22px; height: 22px; border-radius: 50%; background: var(--ginger); }
  .brand-box__name {
    font-family: "Oswald", sans-serif; font-weight: 500; font-size: 46px;
    color: var(--cream); letter-spacing: 1px;
  }
  .speech { position: absolute; left: 0; top: 0; }
  .speech__text {
    position: absolute; left: 57px; top: 352px; width: 470px;
    font-family: "Oswald", sans-serif; font-weight: 500; font-size: 43px;
    line-height: 51.5px; text-align: center; color: var(--cream);
  }
  .pets-shadow {
    position: absolute; left: 596px; top: 890px; width: 580px; height: 22px;
    border-radius: 50%; background: var(--shadow);
  }
  .pets-art {
    position: absolute; left: 680px; top: 520px; width: 472px; height: 384px;
    border-radius: 48% 48% 12px 12px / 60% 60% 12px 12px;
    background: linear-gradient(100deg, var(--ginger) 0%, #e9a25c 42%, var(--chestnut) 58%, #4f2c14 100%);
  }
  .headline {
    position: absolute; left: 130px; top: 782px; width: 960px;
    font-family: "Yellowtail", "Cookie", cursive; font-weight: 400; font-size: 108px; line-height: 1.1;
    text-align: center; color: var(--ink); white-space: nowrap;
  }
  .terms {
    position: absolute; left: 0; top: 918px; width: 1173px;
    font-family: "Open Sans", sans-serif; font-size: 23px; line-height: 35px;
    text-align: center; color: var(--ink);
  }
</style>
</head>
<body>
  <main class="poster">
    <div class="poster__band"></div>

    <div class="brand-box">
      <span class="brand-box__dot"></span>
      <span class="brand-box__name">Vettoly</span>
    </div>

    <svg class="speech" width="1200" height="1200" viewBox="0 0 1200 1200" aria-hidden="true">
      <path fill="var(--cocoa)" d="M304 254 C470 254 585 340 570 470 C565 520 580 565 656 602 C590 608 545 606 505 606 C455 650 385 672 304 672 C154 672 30 578 30 462 C30 346 154 254 304 254 Z"/>
    </svg>
    <p class="speech__text">Refer a fur friend to our friendly team and both your fur child and their fur child will receive a $30 voucher to use in clinic!</p>

    <div class="pets-shadow"></div>
    <div class="pets-art" role="img" aria-label="Illustration of a smiling ginger cat and a brown beagle puppy sitting together"></div>

    <h1 class="headline">We love Pal Spotters!</h1>

    <p class="terms">Limited to one pet per fur parent and the referred fur parent must be new to our clinic.<br>Unlimited vouchers for number of referrals!</p>
  </main>
</body>
</html>
```